Chicago Train Advertisement for HomeAlongRail.com.

We have purchased one month of advertising on the Chicago NRX subway train. We will have 150 cards up in the subway to advertise our website HomeAlongRail.com where people can search for properties by train station. The cards are 11" tall and 46.5" long. We want people to feel compelled to jump on their cell phones and conduct a search for an apartment or home while they are riding the train, or at least enter their email and search criteria so one of our agents can help them.

Target Market(s)

People who want to live near train stations

Industry/Entity Type

Real Estate

Font styles to use
Sans Serif

Colors

Designer to choose colors to be used in the design.

Requirements
Must have
• The homealongrail logo and a catchy slogan, something like: Find your home near a train station the easy way: www.homealongral.com. Search real estate listings near the NRX or Velco.

```html
<!DOCTYPE html>
<html lang="en">
<head>
<meta charset="UTF-8">
<title>HomeAlongRail.com – Train Card</title>
<link rel="stylesheet" href="https://fonts.googleapis.com/css2?family=Open+Sans:ital,wght@0,400;0,600;0,700;0,800;1,800&display=swap">
<style>
  :root {
    --page: #ffffff;
    --navy-deep: #141a4f;
    --navy: #1d2a6b;
    --sky: #2fa3dc;
    --panel-light: #f4f4f5;
    --panel-mid: #d9d9dc;
    --panel-dark: #bfc0c4;
    --bar-white: #ffffff;
    --text-dark: #1c1f3a;
    --photo-sky: #5aa3e6;
    --photo-house: #a49a76;
    --photo-lawn: #5d9a3a;
  }
  * { margin: 0; padding: 0; box-sizing: border-box; }
  html, body { width: 1200px; height: 1200px; overflow: hidden; background: var(--page); }
  body { position: relative; font-family: "Open Sans", Arial, sans-serif; }

  .train-card {
    position: absolute;
    left: 26px; top: 464px;
    width: 1148px; height: 272px;
    overflow: visible;
  }
  .house-photo {
    position: absolute; left: 0; top: 0;
    width: 488px; height: 272px;
    background: linear-gradient(180deg, var(--photo-sky) 0%, #9cc7ea 30%, var(--photo-house) 48%, #8b8466 78%, var(--photo-lawn) 92%, #4f8a30 100%);
  }
  .message-panel {
    position: absolute; left: 488px; top: 0;
    width: 660px; height: 272px;
    background: radial-gradient(ellipse at 50% 35%, var(--panel-light) 0%, var(--panel-mid) 65%, var(--panel-dark) 100%);
  }
  .headline {
    position: absolute; left: 488px; width: 660px; top: 18px;
    text-align: center; line-height: 1;
  }
  .headline-top {
    display: block;
    font-style: italic; font-weight: 800; font-size: 38px;
    color: var(--navy-deep); letter-spacing: -0.5px;
  }
  .headline-top .soft { color: var(--navy); }
  .headline-bottom {
    display: block; margin-top: 6px;
    font-weight: 700; font-size: 33px;
    color: var(--sky); letter-spacing: -0.2px;
  }
  .search-bar {
    position: absolute; left: 406px; top: 107px;
    width: 702px; height: 58px;
    background: var(--bar-white);
    border: 3px solid #dcdde0;
    border-radius: 3px;
    box-shadow: 0 8px 14px rgba(0,0,0,0.28);
    display: flex; align-items: center;
  }
  .search-icon {
    width: 56px; height: 48px; margin-left: 4px;
    background: var(--navy-deep);
    display: flex; align-items: center; justify-content: center;
  }
  .search-text {
    margin-left: 42px;
    font-size: 23px; font-weight: 400; color: var(--text-dark);
  }
  .brand {
    position: absolute; left: 488px; width: 660px; top: 208px;
    display: flex; align-items: center; justify-content: center; gap: 12px;
  }
  .brand-dot {
    width: 34px; height: 34px; border-radius: 50%;
    background: var(--sky);
  }
  .brand-name {
    font-size: 30px; font-weight: 600; color: var(--navy-deep);
    letter-spacing: -0.3px;
  }
</style>
</head>
<body>
  <section class="train-card">
    <div class="house-photo" role="img" aria-label="Photo of a craftsman house with dormers, a wide front porch and green lawn under a blue sky"></div>
    <div class="message-panel"></div>

    <h1 class="headline">
      <span class="headline-top">FIND YOUR HOME <span class="soft">NEAR A</span></span>
      <span class="headline-bottom">TRAIN STATION THE EASY WAY</span>
    </h1>

    <div class="search-bar">
      <div class="search-icon">
        <svg width="34" height="34" viewBox="0 0 34 34" aria-hidden="true">
          <circle cx="20" cy="13" r="9" fill="none" stroke="#ffffff" stroke-width="3.5"/>
          <line x1="13.5" y1="19.5" x2="4" y2="29" stroke="#2fa3dc" stroke-width="5" stroke-linecap="round"/>
        </svg>
      </div>
      <p class="search-text">Search real estate listings near the NRX or Velco.</p>
    </div>

    <div class="brand">
      <span class="brand-dot"></span>
      <span class="brand-name">HomeAlongRail.com</span>
    </div>
  </section>
</body>
</html>
```